A Speech Therapy Business needs to update their logo

I need an update to the font and color of my logo to look more appealing. I am looking to open a private practice as a Speech Language Pathologist that caters to adults and children. It needs to be sophisticated and friendly at the same time. I want to keep the silhouette in my logo as is, just update the font and color for "Brightpaths".
Industry/Entity Type
Business
Contact Information for Business Card
I want the business card to have my logo, my name (Dorota Valk, CCC-SLP, TSSLD) and that I am a Bilingual Speech Language Pathologist. Also, include my phone number, (555) 271-8390. Include my website, Brightpathsslp.example, and email address, dorotavalk@brightpathsslp.example
Look and feel
Each slider illustrates characteristics of the customer's brand and the style your logo design should communicate.

```html
<!DOCTYPE html>
<html lang="en">
<head>
<meta charset="utf-8">
<title>Brightpaths – Business Card</title>
<link rel="stylesheet" href="https://fonts.googleapis.com/css2?family=Source+Sans+3:wght@400;600&display=swap">
<style>
  :root {
    --backdrop: #161616;
    --card-white: #ffffff;
    --brand-red: #e81218;
    --brand-red-soft: #f0403f;
    --ink: #141414;
    --paper: #ffffff;
  }
  * { margin: 0; padding: 0; box-sizing: border-box; }
  html, body {
    width: 1200px; height: 900px; overflow: hidden;
    background: var(--backdrop);
    font-family: "Source Sans 3", "Helvetica Neue", Arial, sans-serif;
  }
  .stage { position: relative; width: 1200px; height: 900px; }
  .card {
    position: absolute; top: 306px; width: 440px; height: 271px;
    border-radius: 12px; overflow: hidden;
  }
  .card-front { left: 149px; background: var(--card-white); }
  .card-back { left: 608px; background: var(--brand-red); }

  .brand-figures { position: absolute; }
  .card-front .brand-figures {
    left: 178px; top: 397px; width: 155px; height: 62px;
    background: linear-gradient(90deg, #1d1d1d, #3a3a3a);
    border-radius: 4px;
  }
  .card-front .brand-figures { left: 29px; top: 91px; }
  .wordmark { position: absolute; font-weight: 400; line-height: 1; white-space: nowrap; }
  .card-front .wordmark {
    left: 30px; top: 153px; font-size: 30px; color: var(--brand-red);
  }

  .contact-block { position: absolute; left: 206px; top: 80px; color: var(--ink); }
  .person-name { font-size: 15px; font-weight: 600; color: var(--brand-red); }
  .person-name .credentials { font-size: 11.5px; }
  .person-role { font-size: 12.5px; margin-top: 1px; }
  .contact-list { list-style: none; margin-top: 27px; font-size: 12.5px; }
  .contact-list li { display: flex; align-items: center; height: 16px; }
  .contact-list svg { width: 9px; height: 9px; margin-right: 7px; flex: none; fill: var(--brand-red); }

  .back-decoration {
    position: absolute; inset: 0;
    background: radial-gradient(ellipse at 30% 60%, rgba(255,255,255,0.08), rgba(255,255,255,0) 60%),
                radial-gradient(ellipse at 85% 75%, rgba(255,255,255,0.07), rgba(255,255,255,0) 50%);
  }
  .card-back .brand-figures {
    left: 100px; top: 67px; width: 240px; height: 84px;
    background: linear-gradient(90deg, rgba(255,255,255,0.92), rgba(255,255,255,0.8));
    border-radius: 6px;
  }
  .card-back .wordmark {
    left: 102px; top: 156px; font-size: 50px; color: var(--paper);
  }
</style>
</head>
<body>
<main class="stage">
  <section class="card card-front" aria-label="Business card front">
    <div class="brand-figures" role="img" aria-label="Logo silhouette of a row of adults and children holding hands"></div>
    <div class="wordmark">Brightpaths</div>
    <div class="contact-block">
      <p class="person-name">Dorota Valk, <span class="credentials">CCC-SLP, TSSLD</span></p>
      <p class="person-role">Bilingual Speech Language Pathologist</p>
      <ul class="contact-list">
        <li><svg viewBox="0 0 10 10" aria-hidden="true"><path d="M2 0.5 L3.8 2.6 L2.8 3.8 Q4 6.2 6.2 7.2 L7.4 6.2 L9.5 8 L8.3 9.5 Q4.5 9.5 2 7 Q0 4.5 0.5 1.7 Z"/></svg>(555) 271-8390</li>
        <li><svg viewBox="0 0 10 10" aria-hidden="true"><path d="M0.5 2 H9.5 V8 H0.5 Z M1 2.4 L5 5.4 L9 2.4" stroke="#fff" stroke-width="0.8"/></svg>dorotavalk@brightpathsslp.example</li>
        <li><svg viewBox="0 0 10 10" aria-hidden="true"><circle cx="5" cy="5" r="4.5"/><path d="M0.8 5 H9.2 M5 0.6 Q2.6 5 5 9.4 M5 0.6 Q7.4 5 5 9.4" stroke="#fff" stroke-width="0.7" fill="none"/></svg>Brightpathsslp.example</li>
      </ul>
    </div>
  </section>

  <section class="card card-back" aria-label="Business card back">
    <div class="back-decoration" role="img" aria-label="Faint enlarged logo silhouettes of people as background decoration"></div>
    <div class="brand-figures" role="img" aria-label="Logo silhouette of a row of adults and children holding hands"></div>
    <div class="wordmark">Brightpaths</div>
  </section>
</main>
</body>
</html>
```